" Iniciamos o projeto do cliente com análise do consumo de energia elétrica, a partir disso dimensionamos o sistema utilizando a melhor solução de energia solar fotovoltaica para o cliente. Elaboramos a proposta do projeto com o orçamento e após aceite do cliente iniciamos o processo de homologação junto às concessionárias e instalação do sistema no cliente com a nossa própria equipe técnica. Também apresentamos o saving e payback do projeto. "

```html
<!DOCTYPE html>
<html lang="pt-BR">
<head>
<meta charset="UTF-8">
<title>Rocha &amp; Brisa — Energia Solar</title>
<link rel="stylesheet" href="https://fonts.googleapis.com/css2?family=Montserrat:wght@500;600;700;800&display=swap">
<style>
  :root {
    --navy: #17324f;
    --orange: #ee6b1f;
    --grey-line: #c9ced4;
    --text-grey: #3a4350;
    --page: #eef0f2;
    --white: #ffffff;
    --sky-top: #5c9fd8;
    --sky-bottom: #1d4f86;
  }
  * { box-sizing: border-box; margin: 0; padding: 0; }
  html, body {
    width: 1200px;
    height: 1200px;
    overflow: hidden;
    background: var(--page);
    font-family: "Montserrat", Arial, sans-serif;
  }
  .banner {
    position: absolute;
    left: 0;
    top: 265px;
    width: 1200px;
    height: 670px;
    background: var(--white);
    overflow: hidden;
  }
  .panel-strip {
    position: absolute;
    left: 740px;
    top: 0;
    width: 460px;
    height: 112px;
    background: linear-gradient(160deg, var(--sky-top) 0%, #3b78b5 55%, var(--sky-bottom) 100%);
    clip-path: polygon(40px 0, 100% 0, 100% 100%, 0 100%);
  }
  .brand {
    position: absolute;
    left: 930px;
    top: 18px;
    width: 256px;
    height: 70px;
    background: var(--white);
    display: flex;
    align-items: center;
    gap: 12px;
    padding: 0 18px;
  }
  .brand-dot {
    width: 28px;
    height: 28px;
    border-radius: 50%;
    background: var(--orange);
    flex: none;
  }
  .brand-name {
    font-weight: 700;
    font-size: 24px;
    color: var(--navy);
    white-space: nowrap;
  }
  .headline {
    position: absolute;
    left: 30px;
    top: 100px;
    font-weight: 800;
    font-size: 37px;
    line-height: 43px;
    color: var(--navy);
    letter-spacing: 0.2px;
  }
  .accent { color: var(--orange); }
  .divider {
    position: absolute;
    left: 0;
    top: 200px;
    width: 820px;
    height: 2px;
    background: var(--grey-line);
  }
  .subline {
    position: absolute;
    left: 30px;
    top: 228px;
    font-weight: 800;
    font-size: 17px;
    line-height: 22px;
    color: var(--navy);
    text-transform: uppercase;
  }
  .bulb {
    position: absolute;
    left: 190px;
    top: 360px;
    width: 300px;
    height: 230px;
  }
  .offer-title {
    position: absolute;
    left: 650px;
    top: 290px;
    font-weight: 700;
    font-size: 44px;
    line-height: 52px;
    color: var(--navy);
  }
  .services {
    position: absolute;
    top: 438px;
    list-style: none;
  }
  .services.col-a { left: 650px; }
  .services.col-b { left: 945px; }
  .services::before {
    content: "";
    position: absolute;
    left: 5px;
    top: 10px;
    bottom: 10px;
    width: 2px;
    background: var(--orange);
  }
  .services li {
    position: relative;
    padding-left: 24px;
    font-weight: 500;
    font-size: 14px;
    line-height: 24px;
    color: var(--text-grey);
    white-space: nowrap;
  }
  .services li::before {
    content: "";
    position: absolute;
    left: 0;
    top: 7px;
    width: 12px;
    height: 12px;
    border-radius: 50%;
    background: var(--orange);
  }
  .footer-band {
    position: absolute;
    left: 0;
    top: 612px;
    width: 1200px;
    height: 28px;
    background: var(--navy);
  }
</style>
</head>
<body>
  <main class="banner">
    <div class="panel-strip" role="img" aria-label="Foto de painéis solares sob céu azul"></div>
    <div class="brand">
      <span class="brand-dot"></span>
      <span class="brand-name">Rocha &amp; Brisa</span>
    </div>

    <h1 class="headline">
      <span class="accent">JÁ IMAGINOU</span> O QUE DA PRA<br>
      FAZER COM <span class="accent">ENERGIA LIVRE?</span>
    </h1>
    <div class="divider"></div>
    <p class="subline">Estamos vivendo uma mudança de paradigma<br>na ralação com energia elétrica.</p>

    <svg class="bulb" viewBox="0 0 300 230" role="img" aria-label="Ilustração de lâmpada com painéis solares e céu azul dentro">
      <defs>
        <linearGradient id="bulbFill" x1="0" y1="0" x2="0" y2="1">
          <stop offset="0" stop-color="#7db8e8"/>
          <stop offset="1" stop-color="#1f5a96"/>
        </linearGradient>
      </defs>
      <rect x="0" y="0" width="300" height="230" rx="0" fill="url(#bulbFill)"/>
    </svg>

    <h2 class="offer-title">O que nós podemos<br><span class="accent">fazer por você hoje?</span></h2>

    <ul class="services col-a">
      <li>Importação de equipamentos</li>
      <li>Acompanhamento de desempenho</li>
      <li>Atendimento as normas e legislações</li>
      <li>Elaboração Guia da Implantação</li>
      <li>Planejamento e Análise de Risco</li>
      <li>Desembaraço junto a concessionária</li>
    </ul>
    <ul class="services col-b">
      <li>Projeto Elétrico Técnico</li>
      <li>Implantação completa</li>
      <li>Otimização de desempenho</li>
      <li>Manutenção</li>
      <li>Projeto e Simulação 3D</li>
      <li>Comissionamento</li>
    </ul>

    <div class="footer-band"></div>
  </main>
</body>
</html>
```